Emergency Dental Referral Company

I need a brochure to advertise my business to prospective dentists that may want to join or to dentists that may want to use this for their own patients. I also need to advertise this brochure to ER physicians who see many dental emergencies. This brochure is meant to be dual purpose: advertise our company and services to the ER physicians who then hand out the brochures to the dental emergency patients in pain. See our website for further details at www.molarrelieffast.net

I will also be attaching our logo design.

Target Market(s)

Emergency Room physicians and other medical personnel who will distribute these brochures to patients in dental pain and dental emergencies

Industry/Entity Type

Business

Font styles to use
Serif
Sans Serif

Requirements
Must have
• Must be simple! Must have a call to action- inspiration to go to website. Highlight our guarantee that states "If you are not seen by a dentist in 24 hours or less, you will receive your money back. Emphasis on the logo. Must discuss how we find a dentist in your zip code in three easy steps.
• For the color- please make similar to our website of www.molarrelieffast.net
Nice to have
• Would like to state that this service can see patients at any hour of the day.
Should not have
• no contact information besides the URL. www.molarrelieffast.net

```html
<!DOCTYPE html>
<html lang="en">
<head>
<meta charset="utf-8">
<title>Molar Relief Fast – Your Emergency Dentist</title>
<link rel="stylesheet" href="https://fonts.googleapis.com/css2?family=Arimo:wght@700&family=Courier+Prime&family=PT+Sans:wght@400;700&display=swap">
<style>
  :root {
    --brand-blue: #29a9e1;
    --text-blue: #2a7fc2;
    --tag-green: #3fa548;
    --url-green: #3aa843;
    --bg-top: #ffffff;
    --bg-bottom: #d3e9f7;
    --photo-light: #eef3f7;
    --photo-mid: #c9d6e0;
  }
  * { margin: 0; padding: 0; box-sizing: border-box; }
  html, body { width: 1200px; height: 927px; overflow: hidden; }
  body { background: #ffffff; }
  .brochure {
    position: relative;
    width: 1200px;
    height: 927px;
    overflow: hidden;
    background: linear-gradient(160deg, var(--bg-top) 0%, #f1f8fd 45%, var(--bg-bottom) 100%);
    font-family: "PT Sans", sans-serif;
  }
  .brand {
    position: absolute;
    display: flex;
    align-items: flex-start;
    color: var(--brand-blue);
    font-family: "Arimo", sans-serif;
    font-weight: 700;
  }
  .brand-dot {
    flex: none;
    border-radius: 50%;
    background: var(--brand-blue);
  }
  .brand-name { line-height: 1; }
  .brand--small { left: 38px; top: 60px; gap: 18px; }
  .brand--small .brand-dot { width: 66px; height: 66px; margin-top: 6px; }
  .brand--small .brand-name { font-size: 48px; }
  .brand--large { left: 466px; top: 62px; gap: 30px; }
  .brand--large .brand-dot { width: 130px; height: 130px; margin-top: 14px; }
  .brand--large .brand-name { font-size: 84px; }
  .tagline {
    position: absolute;
    font-family: "Courier Prime", serif;
    color: var(--tag-green);
    white-space: nowrap;
  }
  .tagline--small { left: 40px; top: 272px; font-size: 24px; letter-spacing: 2px; }
  .tagline--large { left: 468px; top: 376px; font-size: 36px; letter-spacing: 9px; }
  .guarantee {
    position: absolute;
    left: 40px;
    top: 356px;
    width: 390px;
    text-align: center;
    font-weight: 700;
    font-size: 21px;
    line-height: 1.3;
    color: var(--text-blue);
  }
  .site-url {
    position: absolute;
    color: var(--url-green);
    text-align: center;
    white-space: nowrap;
  }
  .site-url--small { left: 40px; top: 496px; width: 390px; font-size: 28px; }
  .site-url--large { left: 470px; top: 842px; width: 682px; font-size: 31px; }
  .hero-photo {
    position: absolute;
    left: 30px;
    top: 583px;
    width: 410px;
    height: 344px;
    background: radial-gradient(ellipse at 50% 45%, var(--photo-light) 0%, var(--photo-mid) 100%);
  }
  .about {
    position: absolute;
    left: 470px;
    top: 484px;
    width: 682px;
    text-align: center;
    color: var(--text-blue);
    font-size: 17.2px;
    line-height: 21.5px;
  }
  .about p + p { margin-top: 21px; }
</style>
</head>
<body>
  <main class="brochure">
    <div class="brand brand--small">
      <span class="brand-dot"></span>
      <span class="brand-name">Molar Relief<br>Fast</span>
    </div>
    <p class="tagline tagline--small">Your Emergency Dentist</p>
    <p class="guarantee">If you are not seen by a dentist in 24 hours or less, you will receive your money back!</p>
    <p class="site-url site-url--small">www.molarrelieffast.net</p>
    <div class="hero-photo" role="img" aria-label="Photo of a smiling man in a white shirt and tie raising his fists in celebration behind a laptop"></div>

    <div class="brand brand--large">
      <span class="brand-dot"></span>
      <span class="brand-name">Molar<br>Relief Fast</span>
    </div>
    <p class="tagline tagline--large">Your Emergency Dentist</p>
    <div class="about">
      <p>Our mission plain and simple is to get you seen by a qualified dentist as quickly as possible to get you out of pain. Nobody likes pain and no one should have to live with it. If we can get you seen by a dentist in 24 hours or less, we have succeeded.</p>
      <p>What we strive for is a quicker, more reliable method for patients to access their dental professional. Going to the local hospitals’ Emergency Department for a tooth ache will not solve the issue, hospitals are often times not equipped to handle dental emergencies and do not have dentists on staff. You leave with antibiotics and pain medication, not a solution to the real underlying problem. Leave here confident, knowing you will see a dentist in less than 24 hours!</p>
    </div>
    <p class="site-url site-url--large">www.molarrelieffast.net</p>
  </main>
</body>
</html>
```